International Clinical Software Company needs a new business card design

We are looking for a new business card design for our company that has recently expanded into the UK market, making us a multinational company.
After having rebranded our website and produced a new style guide, we are looking for a business card that is creative and attention grabbing, while being consistent with the style and colour scheme used on the new website, www.brookvale.example
We produce care management technology for the aged care market, but the main aspect we aim to communicate is the human element of our software, and the way it assists in providing better care for aged people, and stronger relationships between aged people and the staff that care for them.
Our current business card is a dark green with gold text, which makes the text quite difficult to read, not very aesthetically appealing and the colour scheme looks quite dated.
We would like something fresh and modern, that can still be colourful but doesn't use large blocks of dark colour, and uses the colours within our logo.
Something tying in with the leaves that are used in our logo could work quite nicely, along with the Autumn/Fall colours of soft greens, yellows and reds (also in our existing logo). However also happy to look at fresh, completely out of the box ideas we may not have yet considered.
Target Market(s)
The people that receive this business card work in the aged card or health industry and are either corporate/management level staff or clinical (Registered Nurses, care workers etc.)
Industry/Entity Type
Health Product
Contact Information for Business Card
Company Name - BrookvaleTech
Company locations: United Kingdom, Australia, New Zealand
Staff Details:
Staff name: Dermot Quill
Staff job title: Executive Chairman
Staff email: d.quill@brookvale.example
Office phone number: 01632 960418
Font styles to use
Other font styles liked:
- Calibri
Requirements
Must have
- Must include the BrookvaleTech brand name in it's current font
- Must include logo (3 leaves in gold circle)
- Must include Business Card Details
Nice to have
- Elements of gold
- White space
- Something autumn themed but not too cliched
Should not have
- No blue - used by a major competitor and we would like to differentiate from them
- Large blocks of dark green colour (the green that appears in our leaves on the logo on our current business card is the background colour and it is far too dark)

```html
<!DOCTYPE html>
<html lang="en">
<head>
<meta charset="utf-8">
<title>BrookvaleTech Business Card</title>
<link href="https://fonts.googleapis.com/css2?family=Open+Sans:wght@300;400;600&display=swap" rel="stylesheet">
<style>
  :root {
    --backdrop: #ebe7dd;
    --card-white: #fdfdfb;
    --band-khaki: #c4bf94;
    --band-khaki-dark: #a9a47a;
    --gold: #b7ae80;
    --gold-deep: #a59c6c;
    --ink: #2b2b2b;
    --leaf-peach: #f3dfcf;
    --leaf-cream: #f8efe5;
  }
  * { margin: 0; padding: 0; box-sizing: border-box; }
  html, body {
    width: 1200px; height: 780px; overflow: hidden;
    background: var(--backdrop);
    font-family: "Open Sans", "Calibri", sans-serif;
  }
  .canvas {
    position: relative; width: 1200px; height: 780px;
    display: flex; align-items: center; justify-content: center;
  }
  .business-card {
    position: relative; width: 1050px; height: 600px;
    background: var(--card-white);
    overflow: hidden;
    box-shadow: 0 6px 24px rgba(0,0,0,0.12);
  }
  .autumn-foliage {
    position: absolute; top: 0; right: 0; width: 640px; height: 600px;
    background:
      radial-gradient(ellipse at 55% 30%, var(--leaf-peach) 0%, rgba(243,223,207,0.5) 35%, rgba(253,253,251,0) 70%),
      radial-gradient(ellipse at 80% 75%, var(--leaf-cream) 0%, rgba(253,253,251,0) 60%);
    opacity: 0.9;
  }
  .brand-band {
    position: absolute; left: 0; top: 0; width: 170px; height: 600px;
    background: linear-gradient(90deg, var(--band-khaki-dark), var(--band-khaki));
  }
  .band-notch {
    position: absolute; left: 0; top: 170px; width: 170px; height: 85px;
    background: var(--card-white);
  }
  .logo-disc {
    position: absolute; left: 65px; top: 145px; width: 210px; height: 210px;
  }
  .card-details {
    position: absolute; left: 315px; top: 150px;
    color: var(--ink);
  }
  .company-name {
    font-weight: 300; font-size: 68px; line-height: 1;
    color: var(--gold); letter-spacing: 0.5px;
  }
  .company-locations {
    font-size: 19px; margin-top: 8px; color: var(--ink);
  }
  .staff-name {
    font-size: 36px; font-weight: 400; color: var(--gold);
    margin-top: 42px; line-height: 1.1;
  }
  .staff-title { font-size: 22px; line-height: 1.2; }
  .contact-list { list-style: none; margin-top: 34px; }
  .contact-item {
    display: flex; align-items: center; gap: 12px;
    font-size: 21px; line-height: 1.5;
  }
  .contact-icon { width: 24px; height: 24px; flex: none; }
</style>
</head>
<body>
<main class="canvas">
  <article class="business-card">
    <div class="autumn-foliage" role="img" aria-label="Faint background of autumn leaves on branches"></div>
    <div class="brand-band"></div>
    <div class="band-notch"></div>
    <svg class="logo-disc" viewBox="0 0 210 210" aria-hidden="true">
      <circle cx="105" cy="105" r="98" fill="#fdfdfb" stroke="#c4bf94" stroke-width="8"/>
    </svg>
    <section class="card-details">
      <h1 class="company-name">BrookvaleTech</h1>
      <p class="company-locations">United Kingdom, Australia, New Zealand</p>
      <p class="staff-name">Dermot Quill</p>
      <p class="staff-title">Executive Chairman</p>
      <ul class="contact-list">
        <li class="contact-item">
          <svg class="contact-icon" viewBox="0 0 24 24" aria-hidden="true">
            <rect width="24" height="24" fill="#b7ae80"/>
            <rect x="4" y="7" width="16" height="11" fill="none" stroke="#fff" stroke-width="1.6"/>
            <path d="M4 7 L12 13 L20 7" fill="none" stroke="#fff" stroke-width="1.6"/>
          </svg>
          <span>d.quill@brookvale.example</span>
        </li>
        <li class="contact-item">
          <svg class="contact-icon" viewBox="0 0 24 24" aria-hidden="true">
            <rect width="24" height="24" fill="#b7ae80"/>
            <circle cx="12" cy="12" r="7" fill="none" stroke="#fff" stroke-width="1.5"/>
            <ellipse cx="12" cy="12" rx="3" ry="7" fill="none" stroke="#fff" stroke-width="1.2"/>
            <path d="M5 12 H19" stroke="#fff" stroke-width="1.2"/>
          </svg>
          <span>www.brookvale.example</span>
        </li>
      </ul>
    </section>
  </article>
</main>
</body>
</html>
```